Wordpress Design for my Consulting Company

We want a WordPress site created for our new business. We have created a mock-up of the content we want on the site at https://marcobellweather.example.com/website-5

We are not attached to any of the pictures and just put stock stuff from bloq's editor, which we don't have rights to use outside of bloq.

We are NOT looking to just port this site to WordPress, we are looking for some creative ways to display the content in a more professional artistic sense.

I have included several logo files and a text file with the colors and Fonts used in the logo. We are not looking to change the logo or the colors used in the logo.

The Schedule appointment links to a page that embeds a bookslot.example calendar. https://bookslot.example.com/marco-bellweather/trailguide

The final website domain will be venturelanterns.example

Venture lanterns is a consulting company that works directly with the business owners and leaders of small businesses between 50-200 employees. We help companies make sure they have the right technology to meet their strategic goals. We are the anti-"Computer Guy" and we focus on business outcomes NOT cool technology gadgets.

The final design should communicate business growth and success.

Target Market(s)

Business Owners of companies with 50-200 employees

Coding

Coded - Design and coding required

Number of Pages Required

1 page

Font styles to use
Serif
Other font styles liked:
• Trajan Pro Bold, Open Sans

Requirements
Must have
• Should focus on consulting rather than technology.
• Should show the customer as the hero and we are just their guide.
• Must use the logo provided and the colors and fonts in the text file provided. Any other colors and fonts must be complementary.
• The design should scale for all devices computer, iPad, or phone
Should not have
• Should not focus on technology, we are the anti-"Computer Guy" and we focus on business outcomes NOT cool technology gadgets.

```html
<!DOCTYPE html>
<html lang="en">
<head>
<meta charset="utf-8">
<title>Venture lanterns — Technology Advisors That "Get" Business</title>
<link href="https://fonts.googleapis.com/css2?family=Cinzel:wght@400;600;700&family=Open+Sans:wght@300;400;600&display=swap" rel="stylesheet">
<style>
  :root {
    --copper: #c97b4a;
    --slate: #3c4a52;
    --ink: #2e3a40;
    --white: #ffffff;
    --paper: #f8f8f8;
    --dot: #d4d8da;
    --shade: rgba(30, 30, 30, .22);
  }
  * { box-sizing: border-box; margin: 0; padding: 0; }
  html, body { width: 1200px; height: 626px; overflow: hidden; background: var(--white); }
  body { font-family: "Open Sans", Arial, sans-serif; color: var(--ink); }

  .page { position: relative; width: 1200px; height: 626px; overflow: hidden; }

  /* Header */
  .site-header {
    height: 54px; background: var(--paper);
    display: flex; align-items: center; justify-content: space-between;
    padding: 0 195px 0 200px;
  }
  .brand { display: flex; align-items: center; gap: 10px; }
  .brand-mark { width: 28px; height: 28px; border-radius: 50%; background: var(--slate); }
  .brand-name {
    font-family: "Cinzel", Georgia, serif; font-weight: 600; font-size: 12px;
    color: var(--slate); letter-spacing: .4px;
  }
  .main-nav { display: flex; align-items: center; gap: 30px; font-size: 11px; color: var(--ink); }
  .nav-item { display: flex; align-items: center; gap: 8px; }
  .nav-item svg { width: 12px; height: 12px; fill: var(--copper); }

  /* Hero */
  .hero { position: relative; height: 430px; overflow: hidden; }
  .hero-photo {
    position: absolute; inset: 0;
    background:
      linear-gradient(180deg, rgba(0,0,0,0) 55%, rgba(40,32,26,.35) 100%),
      radial-gradient(ellipse 38% 55% at 22% 30%, rgba(230,234,236,.85), rgba(230,234,236,0) 70%),
      radial-gradient(ellipse 30% 50% at 88% 28%, rgba(214,218,220,.55), rgba(214,218,220,0) 70%),
      radial-gradient(ellipse 45% 60% at 70% 65%, rgba(110,80,55,.75), rgba(110,80,55,0) 75%),
      linear-gradient(100deg, #6d7780 0%, #9aa3a9 25%, #a39d95 48%, #7e6a56 68%, #6a5442 85%, #8d8b87 100%);
  }
  .hero-shade { position: absolute; inset: 0; background: var(--shade); }
  .hero-copy {
    position: absolute; left: 415px; top: 158px; width: 400px;
    text-align: center; color: var(--white);
  }
  .hero-title {
    font-weight: 300; font-size: 30px; line-height: 1.02;
    text-transform: uppercase; white-space: nowrap;
  }
  .hero-lead { margin: 12px auto 0; width: 330px; font-size: 14px; font-weight: 300; line-height: 1.05; }
  .btn-schedule {
    display: inline-flex; align-items: center; gap: 8px;
    margin-top: 14px; padding: 6px 18px;
    background: var(--copper); color: var(--white);
    border-radius: 14px; font-size: 11px; font-weight: 600;
    text-transform: uppercase; letter-spacing: .3px;
  }
  .btn-schedule svg { width: 12px; height: 12px; fill: var(--white); }

  /* Value band */
  .value-band { display: flex; height: 84px; }
  .value-we-get {
    flex: 0 0 598px; background: var(--copper); color: var(--white);
    display: flex; align-items: center; justify-content: flex-end; padding-right: 62px;
    font-family: "Cinzel", Georgia, serif; font-weight: 600; font-size: 50px; letter-spacing: .5px;
  }
  .value-slide {
    flex: 1; background: var(--slate); color: var(--white);
    display: flex; align-items: center; padding-left: 58px;
  }
  .value-icon { width: 46px; height: 46px; flex: none; }
  .value-title {
    margin-left: 34px;
    font-family: "Cinzel", Georgia, serif; font-size: 24px; line-height: .98; letter-spacing: .3px;
  }
  .slide-dots { display: flex; gap: 6px; margin-left: 84px; }
  .slide-dots span { width: 8px; height: 8px; border-radius: 50%; background: var(--dot); }
  .slide-dots span.is-active { background: var(--copper); }

  /* Pain points intro */
  .pain-points { position: relative; height: 58px; overflow: hidden; }
  .pain-photo {
    position: absolute; left: 175px; top: 0; width: 423px; height: 100%;
    background:
      radial-gradient(ellipse 30% 90% at 62% 100%, rgba(205,110,80,.55), rgba(205,110,80,0) 70%),
      linear-gradient(180deg, #8e979c 0%, #b3babe 100%);
  }
  .pain-heading {
    position: absolute; left: 632px; top: 18px;
    font-family: "Cinzel", Georgia, serif; font-weight: 400; font-size: 30px;
    color: var(--ink); letter-spacing: .6px; white-space: nowrap;
  }
</style>
</head>
<body>
<div class="page">

  <header class="site-header">
    <div class="brand">
      <span class="brand-mark"></span>
      <span class="brand-name">Venture lanterns</span>
    </div>
    <nav class="main-nav">
      <span class="nav-item">Home</span>
      <span class="nav-item">
        <svg viewBox="0 0 16 16" aria-hidden="true"><path d="M3 2h2V0h2v2h2V0h2v2h2a1 1 0 0 1 1 1v12a1 1 0 0 1-1 1H3a1 1 0 0 1-1-1V3a1 1 0 0 1 1-1zm0 4v9h10V6H3zm2 2h2v2H5V8zm4 0h2v2H9V8z"/></svg>
        Schedule Appointment
      </span>
      <span class="nav-item">
        <svg viewBox="0 0 16 16" aria-hidden="true"><path d="M3.6 1.2l2.2 2.5-1.2 1.8c.9 2 2.4 3.5 4.4 4.4l1.8-1.2 2.5 2.2-1.2 2.7C7 13.3 2.7 9 1 3.1z"/></svg>
        (555) 014-2290
      </span>
    </nav>
  </header>

  <section class="hero">
    <div class="hero-photo" role="img" aria-label="Photo: two business colleagues giving a high five across a meeting table in a bright office"></div>
    <div class="hero-shade"></div>
    <div class="hero-copy">
      <h1 class="hero-title">Technology advisors that<br>"Get" business</h1>
      <p class="hero-lead">We help you leverage technology to create a competitive advantage.</p>
      <span class="btn-schedule">
        <svg viewBox="0 0 16 16" aria-hidden="true"><path d="M3 2h2V0h2v2h2V0h2v2h2a1 1 0 0 1 1 1v12a1 1 0 0 1-1 1H3a1 1 0 0 1-1-1V3a1 1 0 0 1 1-1zm0 4v9h10V6H3zm2 2h2v2H5V8zm4 0h2v2H9V8z"/></svg>
        Schedule Appointment
      </span>
    </div>
  </section>

  <section class="value-band">
    <div class="value-we-get">WE GET...</div>
    <div class="value-slide">
      <svg class="value-icon" viewBox="0 0 40 40" aria-hidden="true" fill="none" stroke="#fff" stroke-width="2">
        <path d="M34 20a14 14 0 1 1-4.1-9.9"/>
        <path d="M30 4v7h-7"/>
        <path d="M15 12h10M15 28h10M16 12c0 5 8 5 8 8s-8 3-8 8M24 12c0 5-8 5-8 8s8 3 8 8"/>
      </svg>
      <div class="value-title">Reducing Time<br>To Decision</div>
      <div class="slide-dots">
        <span class="is-active"></span><span></span><span></span><span></span><span></span><span></span>
      </div>
    </div>
  </section>

  <section class="pain-points">
    <div class="pain-photo" role="img" aria-label="Photo: businessman standing on top of stacked white blocks, looking ahead"></div>
    <h2 class="pain-heading">Are you tired of</h2>
  </section>

</div>
</body>
</html>
```